Real Estate Flyer

Hi - I am assisting a relative to sell a unit. I am looking to have a two page flyer designed (configured as a single page with back to back printing). I have uploaded two samples to give you an idea of the look and feel - one which relates to this property when originally purchased, the other for a different property.
The flyer should includes several key photos on the front along with the wording. The rear should include any secondary photos along with the floor plan.
The flyer should be close to A4 size.

Updates
Hi,
Industry/Entity Type
Real Estate
Look and feel
Each slider illustrates characteristics of the customer's brand and the style your logo design should communicate.

```html
<!DOCTYPE html>
<html lang="en">
<head>
<meta charset="utf-8">
<title>Laurel Street Flyer</title>
<link rel="stylesheet" href="https://fonts.googleapis.com/css2?family=Montserrat:wght@600;700;800&family=Open+Sans:wght@400;600;700&display=swap">
<style>
:root{
  --navy:#274b78;
  --navy-dark:#1f3d63;
  --plan-fill:#2f5688;
  --plan-line:#9fb6d6;
  --accent:#2fa3d6;
  --grey-text:#5a5a5a;
  --silver-1:#f2f2f2;
  --silver-2:#cfd1d3;
  --stage:#d9d9d9;
  --white:#ffffff;
}
*{box-sizing:border-box;margin:0;padding:0}
html,body{width:1200px;height:1000px;overflow:hidden}
body{background:var(--stage);font-family:"Open Sans",Arial,sans-serif;position:relative}
.page{position:absolute;top:91px;width:555px;height:786px;background:var(--white);box-shadow:0 2px 10px rgba(0,0,0,.25);overflow:hidden}
.page--front{left:20px}
.page--back{left:609px}
.page__spine{position:absolute;left:0;top:0;width:20px;height:100%;background:var(--navy)}
.header{position:absolute;left:20px;right:0;top:0;height:54px;background:linear-gradient(180deg,var(--silver-1),var(--silver-2));display:flex;align-items:center;justify-content:space-between;padding:0 12px 0 11px}
.header__address{font-family:"Montserrat",Arial,sans-serif;font-weight:700;font-size:14.5px;color:var(--navy)}
.specs{display:flex;align-items:center;font-family:"Montserrat",Arial,sans-serif;font-weight:700;font-size:15px;color:var(--navy)}
.specs__item{display:flex;align-items:center;gap:2px;padding:0 5px}
.specs__item+.specs__item{border-left:1px solid var(--navy)}
.specs svg{width:18px;height:14px;fill:var(--navy)}
.photo{position:absolute}
.photo__label{position:absolute;background:var(--navy);color:var(--white);font-family:"Montserrat",Arial,sans-serif;font-weight:700;font-size:12.5px;padding:3px 6px;letter-spacing:.3px}
.front-photo{left:20px;top:54px;width:535px;height:322px;background:linear-gradient(180deg,#6aa3e0 0%,#c98a63 45%,#d9c3a6 70%,#3fa8c8 100%)}
.front-rule{position:absolute;left:20px;top:376px;width:535px;height:4px;background:var(--accent)}
.headline{position:absolute;left:37px;top:392px;font-family:"Montserrat",Arial,sans-serif}
.headline__main{font-weight:700;font-size:41px;color:var(--navy);letter-spacing:.6px;line-height:1}
.headline__sub{font-weight:700;font-size:27.5px;color:#606366;letter-spacing:.9px;line-height:1.2}
.intro{position:absolute;left:37px;top:486px;width:500px;font-size:10.8px;line-height:13px;color:var(--grey-text)}
.intro strong{color:var(--navy);font-weight:700}
.features{position:absolute;left:42px;top:578px;list-style:none;font-size:9.4px;line-height:17px;color:var(--grey-text)}
.features li::before{content:"• ";}
.rates{position:absolute;left:40px;top:700px;font-size:9.6px;line-height:13px;font-weight:700;color:var(--navy);display:grid;grid-template-columns:128px 80px;column-gap:21px}
.rates dt{text-align:right}
.info{position:absolute;left:357px;top:568px;width:198px;height:218px;background:var(--navy);color:var(--white);padding:22px 15px}
.info__label{font-family:"Open Sans",Arial,sans-serif;font-weight:700;font-size:13px}
.info__times{font-family:"Open Sans",Arial,sans-serif;font-weight:700;font-size:17px;line-height:20px;margin-top:2px}
.info__rule{height:1px;background:rgba(255,255,255,.4);margin:18px 0 13px}
.info__name{font-family:"Open Sans",Arial,sans-serif;font-weight:700;font-size:16px;line-height:19px;margin-top:2px}
.info__note{font-weight:700;font-size:10.4px;line-height:13px}
.info__phone{font-family:"Open Sans",Arial,sans-serif;font-weight:700;font-size:16px;margin-top:3px}
.balcony-photo{left:20px;top:54px;width:535px;height:310px;background:linear-gradient(135deg,#d9c7a8 0%,#c9a88a 45%,#8fb8df 75%,#5f8f5a 100%)}
.balcony-photo .photo__label{right:2px;top:45px}
.thumb{left:20px;width:240px}
.thumb .photo__label{left:0;top:22px}
.thumb--living{top:368px;height:143px;background:linear-gradient(160deg,#ecebe6,#c9c6bd)}
.thumb--kitchen{top:515px;height:134px;background:linear-gradient(160deg,#efeee9,#bfbcb3)}
.thumb--ensuite{top:653px;height:129px;background:linear-gradient(160deg,#f2f2f0,#c4c6c4)}
.plan{position:absolute;left:264px;top:368px;width:291px;height:418px;background:var(--navy-dark);color:var(--white)}
.plan__drawing{position:absolute;left:14px;top:10px;width:263px;height:336px;background:var(--plan-fill);border:1px dashed var(--plan-line)}
.plan__level{position:absolute;left:0;width:100%;top:264px;text-align:center;font-size:12px;text-decoration:underline;letter-spacing:.3px}
.plan__area{position:absolute;right:22px;top:351px;font-size:7.5px;letter-spacing:.2px}
.plan__footer{position:absolute;left:4px;top:387px;width:240px;font-size:6.5px;font-weight:700;display:flex;justify-content:space-between}
.plan__fine{position:absolute;left:4px;top:397px;width:280px;font-size:4px;line-height:5px;color:rgba(255,255,255,.75)}
.plan__compass{position:absolute;left:6px;top:368px;width:12px;height:12px;border:1px solid var(--plan-line);border-radius:50%}
</style>
</head>
<body>

<section class="page page--front">
  <div class="page__spine"></div>
  <header class="header">
    <span class="header__address">12/40-48 Laurel Street, KESTREL JUNCTION</span>
    <div class="specs">
      <span class="specs__item">2<svg viewBox="0 0 18 14"><rect x="1" y="2" width="2" height="11"/><rect x="1" y="8" width="16" height="3"/><rect x="15" y="8" width="2" height="5"/><rect x="4" y="5" width="4" height="3" rx="1"/><rect x="9" y="5" width="8" height="3" rx="1"/></svg></span>
      <span class="specs__item">1<svg viewBox="0 0 18 14"><rect x="1" y="6" width="16" height="2"/><path d="M2 8h14l-1.5 4h-11z"/><rect x="2" y="1" width="2" height="5"/><rect x="2" y="1" width="4" height="1.5"/></svg></span>
      <span class="specs__item">1<svg viewBox="0 0 18 14"><path d="M3 6l2-4h8l2 4h1v5h-2v2h-2v-2H6v2H4v-2H2V6z"/></svg></span>
    </div>
  </header>
  <div class="photo front-photo" role="img" aria-label="Outdoor pool and sun terrace in front of the brick apartment tower"></div>
  <div class="front-rule"></div>
  <h1 class="headline">
    <span class="headline__main">OVERSIZED</span><br>
    <span class="headline__sub">apartment in a lifestyle location</span>
  </h1>
  <p class="intro"><strong>Peacefully positioned</strong> on the 5th floor of a refurbished security building, this superbly spacious residence combines modern, low maintenance apartment living with inviting prospects for the entertainer.<br>Boasting a huge full-width terrace on-title, its sought-after setting in the heart of Kestrel Junction offers the ultimate in lifestyle and convenience.</p>
  <ul class="features">
    <li>Expansive open plan living and dining area</li>
    <li>Terrace features city and Botany Bay glimpses</li>
    <li>Kitchen updated with Velora gas appliances</li>
    <li>Built-ins in both bedrooms, fully tiled bathrooms</li>
    <li>Internal laundry, secure parking, lift, outdoor pool and gymnasium</li>
    <li>Steps to station, Eastgate Plaza and Parkside Gardens</li>
  </ul>
  <dl class="rates">
    <dt>Estimated Market Rental:</dt><dd>$700.00 p/w</dd>
    <dt>Water Rates:</dt><dd></dd>
    <dt>Council Rates:</dt><dd></dd>
    <dt>Strata Rates:</dt><dd></dd>
  </dl>
  <aside class="info">
    <div class="info__label">Inspect :</div>
    <div class="info__times">Sat 10:45 – 11:30;<br>Wed 12:00 – 12:30</div>
    <div class="info__rule"></div>
    <div class="info__label">Contact:</div>
    <div class="info__name">Daniel Marlow</div>
    <div class="info__note">(Assisting owner in Private Sale)</div>
    <div class="info__phone">0400 555 018</div>
  </aside>
</section>

<section class="page page--back">
  <div class="page__spine"></div>
  <header class="header">
    <span class="header__address">12/40-48 Laurel Street, KESTREL JUNCTION</span>
    <div class="specs">
      <span class="specs__item">2<svg viewBox="0 0 18 14"><rect x="1" y="2" width="2" height="11"/><rect x="1" y="8" width="16" height="3"/><rect x="15" y="8" width="2" height="5"/><rect x="4" y="5" width="4" height="3" rx="1"/><rect x="9" y="5" width="8" height="3" rx="1"/></svg></span>
      <span class="specs__item">1<svg viewBox="0 0 18 14"><rect x="1" y="6" width="16" height="2"/><path d="M2 8h14l-1.5 4h-11z"/><rect x="2" y="1" width="2" height="5"/><rect x="2" y="1" width="4" height="1.5"/></svg></span>
      <span class="specs__item">1<svg viewBox="0 0 18 14"><path d="M3 6l2-4h8l2 4h1v5h-2v2h-2v-2H6v2H4v-2H2V6z"/></svg></span>
    </div>
  </header>
  <div class="photo balcony-photo" role="img" aria-label="Curved balcony with glass balustrade and district views">
    <span class="photo__label">BALCONY</span>
  </div>
  <div class="photo thumb thumb--living" role="img" aria-label="Open plan living and dining room">
    <span class="photo__label">LIVING/DINING</span>
  </div>
  <div class="photo thumb thumb--kitchen" role="img" aria-label="White kitchen with gas cooktop">
    <span class="photo__label">KITCHEN</span>
  </div>
  <div class="photo thumb thumb--ensuite" role="img" aria-label="Tiled ensuite bathroom">
    <span class="photo__label">ENSUITE</span>
  </div>
  <div class="plan">
    <div class="plan__drawing" role="img" aria-label="Level five floor plan: two balconies, main bedroom, bedroom two, kitchen, living and dining, ensuite, laundry and car space"></div>
    <div class="plan__level">LEVEL FIVE</div>
    <div class="plan__area">APPROX : GROSS INTERNAL AREA :- 104 SQM</div>
    <div class="plan__compass"></div>
    <div class="plan__footer"><span>12/40-48 LAUREL STREET</span><span>KESTREL JUNCTION</span></div>
    <p class="plan__fine">Floor Plan Disclaimer: plan is for guide only, sizes are approximate and intending buyers should rely on their own enquiries. Plan prepared for marketing use only.</p>
  </div>
</section>

</body>
</html>
```